Empower our Electric Journey on the Web

We need a new website that can promote our services. Our three services that we offer are:
- Management of e-mobility charging stations
- Management of energy purchases
- Leasing of E-Mobility charging stations
- Energy billing of private electricity meters
The website should work responsively on PC, tablet and smartphone. In general, a simple navigation and an appealing design should be in the foreground. The website should give the customer the possibility to request , based pm a preset chexkbox chart and to get in contact with us.
Our logo works on black and white background.
Our slogan is:
Empower Your Electric Journey with Velmor Mobility
The 4 Pages should be the following:
Main Page, with info about us, why choose us,
2nd; services; what we sell and what are our services
3rd; Contact us, request an offer
4th, References about costumers and Work we already did, in the future we would like to integrate a Blog Post in this section in stead of references.

Target Market(s)

Landlords, Homeowners, Homeowner Associations

Industry/Entity Type

EV Chargers / E-Mobility

Coding

Coded - Design and coding required

Number of Pages Required

4 page

Requirements
Nice to have
• Pop up to our mailchimp newsletter subscription

```html
<!DOCTYPE html>
<html lang="en">
<head>
<meta charset="utf-8">
<title>Velmor Mobility — Smart Electric Car Charging</title>
<link href="https://fonts.googleapis.com/css2?family=Lexend:wght@300;400;500;600;700&family=Poppins:ital,wght@0,400;0,500;0,600;1,400&display=swap" rel="stylesheet">
<style>
:root{
  --green:#42d544;
  --green-deep:#34b936;
  --green-soft:#a9ec9f;
  --ink:#1d1d1d;
  --dark:#232323;
  --grey:#555;
  --white:#ffffff;
  --line:#e3e3e3;
}
*{box-sizing:border-box;margin:0;padding:0}
html,body{width:1200px;height:4118px;overflow:hidden}
body{font-family:"Lexend",sans-serif;color:var(--ink);background:var(--white);position:relative}
.abs{position:absolute}
section,header,footer{position:absolute;left:0;width:1200px}

/* hero */
.hero{top:0;height:587px;overflow:hidden}
.hero-photo{position:absolute;inset:0;background:linear-gradient(100deg,#3b3531 0%,#54504b 35%,#6d6e6c 55%,#3a3a3a 100%)}
.hero-shade{position:absolute;inset:0;background:linear-gradient(90deg,rgba(0,0,0,.15),rgba(0,0,0,.55))}
.brand{display:flex;align-items:center;gap:10px;color:var(--white);font-weight:600;font-size:22px;letter-spacing:2px;text-transform:uppercase}
.brand i{display:block;width:22px;height:22px;background:var(--green)}
.nav{position:absolute;top:19px;left:535px;display:flex;align-items:center;font-size:14px;font-weight:500;color:var(--white)}
.nav a{color:inherit;text-decoration:none}
.nav .active{background:var(--green);border-radius:20px;width:105px;height:35px;display:flex;align-items:center;justify-content:center}
.kicker{left:539px;top:156px;font-size:11.5px;color:var(--white);font-weight:500;letter-spacing:.2px}
.hero h1{position:absolute;left:538px;top:172px;font-size:46px;line-height:54px;color:var(--white);font-weight:700;width:520px}
.hero-text{left:539px;top:362px;width:480px;font-size:14px;line-height:23px;color:var(--white);font-weight:500}
.btn{display:flex;align-items:center;justify-content:center;background:var(--green);color:var(--ink);font-weight:500;font-size:12px;text-decoration:none}
.arrow{position:absolute}

/* about */
.about{top:587px;height:680px}
.about-band{left:862px;top:0;width:338px;height:578px;background:linear-gradient(180deg,#5fd657,#52cf4a 60%,#4bc943)}
.about-photo{left:707px;top:80px;width:376px;height:418px;background:linear-gradient(160deg,#2d3a25,#6a6a62 45%,#3c4a30)}
.about-badge{left:640px;top:104px;width:203px;height:239px;background:var(--green);border:4px solid var(--white)}
.eyebrow{font-size:12px;color:var(--green-deep);text-transform:uppercase;font-weight:500}
.about h2{left:112px;top:120px;font-size:27px;line-height:32px;font-weight:600;width:500px}
.about .lead{left:112px;top:198px;width:500px;font-size:13.5px;line-height:22px;font-weight:500}
.feature{left:114px;width:510px;display:flex;gap:14px}
.ficon{width:80px;height:69px;border:2px solid var(--green);border-radius:6px;flex:none;display:flex;align-items:center;justify-content:center}
.feature h3{font-size:16px;font-weight:500;margin-top:8px}
.feature p{font-size:12.5px;line-height:21px;color:var(--grey);margin-top:2px}

/* why */
.why{top:1267px;height:581px;overflow:hidden}
.why-photo{position:absolute;inset:0;background:linear-gradient(110deg,#22442a,#2b5a31 40%,#3e6f3c 65%,#20391f)}
.why h2{position:absolute;top:68px;width:100%;text-align:center;color:var(--white);font-size:25px;font-weight:500}
.why-card{position:absolute;width:271px;height:70px;background:var(--white);display:flex;align-items:center;gap:12px;padding:0 10px}
.why-card.left{left:118px;justify-content:flex-end;text-align:right}
.why-card.right{left:826px}
.why-card h4{font-size:12.5px;color:var(--green-deep);font-weight:500}
.why-card p{font-size:11px;line-height:15px;color:#333;margin-top:2px}
.wicon{width:52px;height:48px;border:1.5px solid #888;border-radius:4px;flex:none;display:flex;align-items:center;justify-content:center}
.why-circle{position:absolute;left:427px;top:154px;width:352px;height:352px;border-radius:50%;background:radial-gradient(circle at 50% 40%,#c3f3b7,#8fdf7e);border:6px solid var(--green)}

/* solutions */
.solutions{top:1848px;height:816px;background:var(--dark);color:var(--white)}
.solutions h2{left:112px;top:86px;font-size:22px;font-weight:500}
.solutions .sub{left:112px;top:120px;width:560px;font-size:13.5px;line-height:20px;font-weight:500}
.solutions .body{left:112px;top:188px;width:530px;font-size:14px;line-height:22px;color:#d6d6d6;font-weight:300}
.btn-outline{border:1.5px solid var(--white);background:transparent;color:var(--white)}
.svc-img{position:absolute;top:314px;width:304px;height:337px}
.svc-card{position:absolute;top:555px;width:261px;height:165px;background:var(--white);color:var(--ink);text-align:center}
.svc-card .ic{position:absolute;left:50%;top:-38px;margin-left:-36px;width:72px;height:72px;border-radius:50%;background:var(--green-soft);border:4px solid var(--white);display:flex;align-items:center;justify-content:center}
.svc-card .ic span{width:54px;height:54px;border-radius:50%;background:var(--green);display:flex;align-items:center;justify-content:center}
.svc-card h3{margin-top:44px;font-size:20px;font-weight:500}
.svc-card p{font-size:12px;line-height:19px;color:#333;margin:8px 16px 0}
.svc-card a{display:inline-block;margin-top:8px;font-size:11px;font-weight:600;color:var(--green-deep);text-decoration:underline}

/* testimonials */
.testi{top:2664px;height:704px}
.testi-photo{left:112px;top:69px;width:448px;height:382px;background:linear-gradient(170deg,#6c4a3a,#8a6d5e 40%,#b9b4ad 65%,#8b5e4b);border-top-right-radius:28px}
.testi .label{left:613px;top:88px;font-size:15px;font-weight:500}
.testi h2{left:612px;top:110px;font-size:31px;line-height:35px;font-weight:500;width:470px}
.testi .intro{left:613px;top:190px;width:440px;font-size:11.5px;line-height:17px;color:var(--grey);font-family:"Poppins",sans-serif}
.quote-box{left:613px;top:242px;width:427px;height:153px;background:var(--green);border-bottom-left-radius:8px}
.quote-box p{position:absolute;left:36px;top:42px;width:330px;font-family:"Poppins",sans-serif;font-style:italic;font-size:15px;line-height:22px;color:var(--white)}
.quote-mark{left:637px;top:226px;width:46px;height:46px;border-radius:50%;background:var(--green);border:3px solid var(--white);color:var(--white);font-size:32px;font-weight:700;display:flex;align-items:center;justify-content:center;line-height:1;padding-top:12px}
.avatar{left:634px;top:410px;width:54px;height:54px;border-radius:50%;background:linear-gradient(160deg,#c9a07a,#7a5036)}
.person{left:699px;top:423px}
.person b{display:block;font-size:13px;font-weight:500}
.person span{font-size:10px;color:#444}

/* contact */
.contact-band{top:3368px;height:750px;background:var(--dark)}
.map{left:112px;top:3203px;width:499px;height:402px;background:linear-gradient(135deg,#eef0ec,#e1e5df 50%,#eceee9);border-bottom-left-radius:8px}
.form{left:611px;top:3203px;width:479px;height:402px;background:var(--green);border-radius:0 10px 10px 0}
.form h2{position:absolute;left:23px;top:40px;font-size:24px;color:var(--white);font-weight:500}
.field{position:absolute;background:var(--white);font-size:10px;font-weight:600;padding:14px 12px}
.submit{position:absolute;left:298px;top:320px;width:160px;height:42px;background:#8de37f;color:var(--ink);font-size:13px;font-weight:500;display:flex;align-items:center;justify-content:center}

/* footer */
.footer-brand{left:117px;top:3700px}
.foot-about{left:117px;top:3755px;width:240px;font-size:11.5px;line-height:19px;color:#e4e4e4;font-weight:300}
.socials{left:117px;top:3854px;display:flex;gap:10px}
.socials i{display:block;width:14px;height:14px;border-radius:50%;border:2px solid var(--green)}
.vbar{position:absolute;width:3px;height:22px;background:var(--green)}
.vsep{position:absolute;width:1px;background:#3c3c3c}
.col-title{position:absolute;font-size:15px;color:var(--green);font-weight:500}
.links{position:absolute;list-style:none;font-size:13px;color:var(--white);font-weight:500}
.links li{height:39px;display:flex;align-items:center;gap:6px}
.links li::before{content:"→";color:var(--green);font-size:12px}
.qc{position:absolute;color:var(--white);font-size:12px;font-weight:300;line-height:19px}
.qc-row{position:absolute;left:848px;display:flex;align-items:center;gap:10px;color:var(--white);font-size:13.5px;font-weight:500}
.copy{left:112px;top:4078px;font-size:12px;color:var(--white);font-weight:500}
.copy b{color:var(--green);font-weight:500}
.totop{left:981px;top:4070px;font-size:13px;color:var(--white);font-weight:500;display:flex;align-items:center;gap:12px}
</style>
</head>
<body>

<!-- Hero -->
<header class="hero">
  <div class="hero-photo" role="img" aria-label="Photo of an electric car plugged into a charging post in front of a brick building"></div>
  <div class="hero-shade"></div>
  <div class="brand abs" style="left:112px;top:25px"><i></i>Velmor Mobility</div>
  <nav class="nav">
    <a class="active" href="#">Home</a>
    <a href="#" style="margin-left:30px">Services</a>
    <a href="#" style="margin-left:60px">About Costumers</a>
    <a href="#" style="margin-left:62px">Contact Us</a>
  </nav>
  <svg class="arrow" style="left:72px;top:282px" width="76" height="32" viewBox="0 0 76 32"><path d="M74 16H6M20 3L5 16l15 13" fill="none" stroke="#42d544" stroke-width="6" stroke-linecap="round" stroke-linejoin="round"/></svg>
  <svg class="arrow" style="left:1054px;top:282px" width="76" height="32" viewBox="0 0 76 32"><path d="M2 16h68M56 3l15 13-15 13" fill="none" stroke="#42d544" stroke-width="6" stroke-linecap="round" stroke-linejoin="round"/></svg>
  <p class="kicker abs">UNKNOWN PRINTER TOOK A GALLEY OF TYPE AND SCRAMBLED IT TO MAKE A</p>
  <h1>Future Solutions for Smart Electric Car Charging !!</h1>
  <p class="hero-text abs">Unknown printer took a galley of type and scrambled it to make a type specimen book. It has survived not only five centuries.</p>
  <a class="btn abs" href="#" style="left:540px;top:437px;width:221px;height:43px">Explore Charging Solutions</a>
  <a class="btn abs" href="#" style="left:771px;top:437px;width:126px;height:43px">More Abou Us</a>
</header>

<!-- About -->
<section class="about">
  <div class="about-band abs" role="img" aria-label="Faded photo of charging stations tinted green"></div>
  <div class="about-photo abs" role="img" aria-label="Photo of a wall-mounted EV charger with its cable plugged in, hedge behind"></div>
  <div class="about-badge abs"></div>
  <p class="eyebrow abs" style="left:112px;top:102px">About Us</p>
  <span class="abs" style="left:182px;top:111px;width:122px;height:1px;background:var(--green)"></span>
  <h2 class="abs">We Provide Best Charging Services For Your EV</h2>
  <p class="lead abs">Unknown printer took a galley of type and scrambled it to make a type specimen book. It has survived not only five centuries.</p>
  <div class="feature abs" style="top:301px">
    <div class="ficon"><svg width="50" height="34" viewBox="0 0 50 34" fill="none" stroke="#333" stroke-width="1.6"><path d="M4 24v-6l5-7h22l6 7h7v6z"/><circle cx="13" cy="25" r="4"/><circle cx="36" cy="25" r="4"/><path d="M38 10V4h6M44 4v8"/></svg></div>
    <div><h3>Charging Your EVs</h3><p>Lorem Ipsum is simply dummy It is a long established fact that a reader will be distracted by the readable.</p></div>
  </div>
  <div class="feature abs" style="top:409px">
    <div class="ficon"><svg width="50" height="40" viewBox="0 0 50 40" fill="none" stroke="#333" stroke-width="1.6"><path d="M4 30v-6l5-7h22l6 7h7v6z"/><circle cx="13" cy="31" r="4"/><circle cx="36" cy="31" r="4"/><path d="M24 2l-6 10h6l-4 9" stroke="#42d544" stroke-width="2.4"/></svg></div>
    <div><h3>0-80% Charge In 60 Minutes</h3><p>Simply dummy It is a long established fact that a reader will be distracted by the of a when looking at its layout.</p></div>
  </div>
</section>

<!-- Why choose us -->
<section class="why">
  <div class="why-photo" role="img" aria-label="Photo of cars at a charging station under a dark green tint"></div>
  <h2>Why choose Us</h2>
  <svg class="abs" style="left:0;top:0" width="1200" height="581" viewBox="0 0 1200 581">
    <g stroke="#42d544" stroke-width="1.5" fill="#42d544">
      <line x1="389" y1="202" x2="482" y2="202"/><circle cx="482" cy="202" r="6"/>
      <line x1="389" y1="288" x2="432" y2="288"/><circle cx="432" cy="288" r="6"/>
      <line x1="389" y1="374" x2="433" y2="374"/><circle cx="433" cy="374" r="6"/>
      <line x1="389" y1="461" x2="486" y2="461"/><circle cx="486" cy="461" r="6"/>
      <line x1="716" y1="195" x2="826" y2="195"/><circle cx="716" cy="195" r="6"/>
      <line x1="773" y1="283" x2="826" y2="283"/><circle cx="773" cy="283" r="6"/>
      <line x1="775" y1="368" x2="826" y2="368"/><circle cx="775" cy="368" r="6"/>
      <line x1="734" y1="448" x2="826" y2="448"/><circle cx="734" cy="448" r="6"/>
    </g>
  </svg>
  <div class="why-circle" role="img" aria-label="Round photo of a charging station in green tones"></div>

  <div class="why-card left" style="top:167px"><div><h4>Ongoing Maintenance</h4><p>Simply dummy It is a long<br>established fact.</p></div><div class="wicon"><svg width="30" height="30" viewBox="0 0 30 30" fill="none" stroke="#444" stroke-width="1.5"><circle cx="15" cy="15" r="11"/><path d="M10 19l8-8M12 11h6v6" stroke="#42d544"/></svg></div></div>
  <div class="why-card left" style="top:253px"><div><h4>Spare Parts Management</h4><p>Simply dummy It is a long<br>established fact.</p></div><div class="wicon"><svg width="30" height="30" viewBox="0 0 30 30" fill="none" stroke="#444" stroke-width="1.5"><rect x="8" y="4" width="14" height="22" rx="2"/><path d="M16 9l-3 6h4l-3 6" stroke="#42d544"/></svg></div></div>
  <div class="why-card left" style="top:339px"><div><h4>Expert Partner Support</h4><p>Simply dummy It is a long<br>established fact.</p></div><div class="wicon"><svg width="30" height="30" viewBox="0 0 30 30" fill="none" stroke="#444" stroke-width="1.5"><path d="M15 3l10 5v7c0 6-5 10-10 12C10 25 5 21 5 15V8z"/><path d="M16 9l-3 6h4l-3 6" stroke="#42d544"/></svg></div></div>
  <div class="why-card left" style="top:426px"><div><h4>Preventive Maintenance</h4><p>Simply dummy It is a long<br>established fact.</p></div><div class="wicon"><svg width="32" height="30" viewBox="0 0 32 30" fill="none" stroke="#444" stroke-width="1.5"><path d="M3 20v-5l4-6h16l5 6v5z"/><circle cx="9" cy="21" r="3"/><circle cx="23" cy="21" r="3"/><path d="M22 4l6 6" stroke="#42d544"/></svg></div></div>

  <div class="why-card right" style="top:160px"><div class="wicon"><svg width="30" height="30" viewBox="0 0 30 30" fill="none" stroke="#444" stroke-width="1.5"><rect x="7" y="4" width="12" height="22"/><path d="M19 12h4v9h3M13 9l-2 5h3l-2 5" /></svg></div><div><h4>Warranty Extensions</h4><p>Simply dummy It is a long<br>established fact.</p></div></div>
  <div class="why-card right" style="top:248px"><div class="wicon"><svg width="32" height="30" viewBox="0 0 32 30" fill="none" stroke="#444" stroke-width="1.5"><path d="M3 22v-5l4-6h16l5 6v5z"/><circle cx="9" cy="23" r="3"/><circle cx="23" cy="23" r="3"/><circle cx="16" cy="8" r="5" stroke="#42d544"/></svg></div><div><h4>Technical Training</h4><p>Simply dummy It is a long<br>established fact.</p></div></div>
  <div class="why-card right" style="top:333px"><div class="wicon"><svg width="30" height="30" viewBox="0 0 30 30" fill="none" stroke="#444" stroke-width="1.5"><rect x="5" y="5" width="20" height="20" rx="3"/><path d="M9 17h12M11 12h8"/></svg></div><div><h4>On Site Commissioning</h4><p>Simply dummy It is a long<br>established fact.</p></div></div>
  <div class="why-card right" style="top:413px"><div class="wicon"><svg width="30" height="30" viewBox="0 0 30 30" fill="none" stroke="#444" stroke-width="1.5"><rect x="5" y="6" width="14" height="18"/><path d="M19 12h5v8M9 11h6M9 15h6"/></svg></div><div><h4>Easy Management</h4><p>Simply dummy It is a long<br>established fact.</p></div></div>
</section>

<!-- Solutions -->
<section class="solutions">
  <h2 class="abs">EV Charging Solutions For Every Business &amp; Driver.</h2>
  <p class="sub abs">Unknown printer took a galley of type and scrambled it to make a type specimen book. It has survived not only five centuries.</p>
  <p class="body abs">Lorem Ipsum is simply dummy It is a long established fact that a reader will be distracted by the readable content of a page when looking at its layout.</p>
  <a class="btn abs" href="#" style="left:720px;top:198px;width:174px;height:47px;font-size:11px;color:var(--white)">How Does It Work? &nbsp;➔</a>
  <a class="btn btn-outline abs" href="#" style="left:914px;top:198px;width:177px;height:47px;font-size:11px">Check All Solutions &nbsp;➔</a>

  <div class="svc-img" style="left:112px;background:linear-gradient(160deg,#d9a23b,#3a5f9a 45%,#1b2d55)" role="img" aria-label="Photo of a blue car being charged at night"></div>
  <div class="svc-img" style="left:446px;background:linear-gradient(160deg,#c9c2b6,#7d8fa3 45%,#5b5650)" role="img" aria-label="Photo of a woman plugging a charger into a white car"></div>
  <div class="svc-img" style="left:787px;background:linear-gradient(160deg,#b8bd9c,#6a6e6d 50%,#3c3e3f)" role="img" aria-label="Photo of the rear of an electric car parked at a charger"></div>

  <div class="svc-card" style="left:134px"><div class="ic"><span><svg width="28" height="28" viewBox="0 0 28 28" fill="none" stroke="#fff" stroke-width="1.8"><rect x="8" y="3" width="12" height="20" rx="2"/><path d="M15 8l-3 5h4l-3 5"/></svg></span></div><h3>Service 01</h3><p>Lorem Ipsum is simply dummy It is a long established fact that</p><a href="#">READ MORE</a></div>
  <div class="svc-card" style="left:467px"><div class="ic"><span><svg width="28" height="28" viewBox="0 0 28 28" fill="none" stroke="#fff" stroke-width="1.8"><path d="M14 25s-8-8-8-14a8 8 0 0116 0c0 6-8 14-8 14z"/><path d="M15 7l-3 4h4l-3 4"/></svg></span></div><h3>Service 02</h3><p>Lorem Ipsum is simply dummy It is a long established fact that</p><a href="#">READ MORE</a></div>
  <div class="svc-card" style="left:810px"><div class="ic"><span><svg width="28" height="28" viewBox="0 0 28 28" fill="none" stroke="#fff" stroke-width="1.8"><rect x="4" y="4" width="9" height="18"/><path d="M13 12h4v8M18 16l4-3h3v6h-7z"/></svg></span></div><h3>Service 03</h3><p>Lorem Ipsum is simply dummy It is a long established fact that</p><a href="#">READ MORE</a></div>
</section>

<!-- Testimonials -->
<section class="testi">
  <div class="testi-photo abs" role="img" aria-label="Photo of a white electric car charging at a post beside a brick building"></div>
  <p class="label abs">Our Testimonials</p>
  <h2 class="abs">Charging Solutions For All Businesses &amp; EV Drivers.</h2>
  <p class="intro abs">You'd think after creating the world's largest and most open EV charging network we'd be satisfied, but you'd be wrong</p>
  <div class="quote-box abs"><p>“Lorem ipsum is simply dummy It is a long established fact that a reader will be distracted by the readable”</p></div>
  <div class="quote-mark abs">“</div>
  <div class="avatar abs" role="img" aria-label="Customer portrait"></div>
  <div class="person abs"><b>Daniel Reyes Jr</b><span>Dust Manager</span></div>
  <svg class="abs" style="left:956px;top:476px" width="40" height="20" viewBox="0 0 40 20"><path d="M38 10H4M12 3L3 10l9 7" fill="none" stroke="#42d544" stroke-width="3" stroke-linecap="round" stroke-linejoin="round"/></svg>
  <svg class="abs" style="left:1002px;top:476px" width="40" height="20" viewBox="0 0 40 20"><path d="M2 10h34M28 3l9 7-9 7" fill="none" stroke="#1d1d1d" stroke-width="3" stroke-linecap="round" stroke-linejoin="round"/></svg>
</section>

<!-- Contact -->
<div class="contact-band abs" style="left:0;width:1200px"></div>
<div class="map abs" role="img" aria-label="Street map showing the office location"></div>
<form class="form abs">
  <h2>Get in Touch</h2>
  <div class="field" style="left:23px;top:87px;width:211px;height:41px">Name :</div>
  <div class="field" style="left:245px;top:87px;width:213px;height:41px">Phome :</div>
  <div class="field" style="left:23px;top:141px;width:211px;height:42px">Email :</div>
  <div class="field" style="left:245px;top:141px;width:213px;height:42px">Subject :</div>
  <div class="field" style="left:23px;top:195px;width:435px;height:117px">Comments :</div>
  <div class="submit">Submit Now</div>
</form>

<!-- Footer -->
<footer style="top:0;height:0">
  <div class="brand abs footer-brand" style="font-size:21px"><i></i>Velmor Mobility</div>
  <p class="foot-about abs">Duis aute irure dolor in reprehenderit in voluptate velit esse cillum<br>Excepteur sint occaecat cupidatat non proident, sunt in culpa qui officia.</p>
  <div class="socials abs"><i></i><i></i><i></i><i></i></div>

  <span class="vsep" style="left:374px;top:3688px;height:340px"></span>
  <span class="vsep" style="left:571px;top:3688px;height:340px"></span>
  <span class="vsep" style="left:818px;top:3688px;height:340px"></span>
  <span class="vbar" style="left:373px;top:3720px"></span>
  <span class="vbar" style="left:570px;top:3720px"></span>
  <span class="vbar" style="left:817px;top:3720px"></span>

  <p class="col-title" style="left:408px;top:3686px">Sitemap</p>
  <ul class="links" style="left:405px;top:3710px"><li>Home</li><li>Services</li><li>About Costumers</li><li>Contact Us</li></ul>

  <p class="col-title" style="left:602px;top:3686px">Solutions</p>
  <ul class="links" style="left:599px;top:3709px"><li>Business &amp; Commercial</li><li>Fleets &amp; Automakers</li><li>Drivers &amp; Personal Use</li><li>Government &amp; Utilities</li><li>Public Charging Stations</li><li>Battery Maintenance</li></ul>

  <p class="col-title" style="left:848px;top:3686px">Quick Contact</p>
  <p class="qc" style="left:848px;top:3720px;width:250px">If you have any questions or need help, feel free to contact with our team.</p>
  <div class="qc-row" style="top:3776px"><svg width="18" height="13" viewBox="0 0 18 13"><rect width="18" height="13" fill="#42d544"/><path d="M1 1l8 6 8-6" fill="none" stroke="#232323" stroke-width="1.5"/></svg>hello@velmormobility.com</div>
  <div class="qc-row" style="top:3810px"><svg width="16" height="16" viewBox="0 0 24 24"><path d="M6.6 10.8a15 15 0 006.6 6.6l2.2-2.2a1 1 0 011-.25 11.4 11.4 0 003.6.57 1 1 0 011 1V20a1 1 0 01-1 1A17 17 0 013 4a1 1 0 011-1h3.5a1 1 0 011 1c0 1.25.2 2.45.57 3.6a1 1 0 01-.25 1z" fill="#42d544"/></svg>02 0100 555 0147</div>
  <p class="qc" style="left:848px;top:3848px;width:200px;font-size:11px;line-height:16px">418 Alder Lane Brookfield, New York 11000 United States</p>
  <div class="qc-row" style="top:3893px;color:var(--green);font-size:13px"><svg width="11" height="14" viewBox="0 0 12 16"><path d="M6 16S0 9 0 6a6 6 0 0112 0c0 3-6 10-6 10z" fill="#42d544"/><circle cx="6" cy="6" r="2" fill="#232323"/></svg>Get Directions</div>

  <p class="copy abs">©2023 <b>VELMOR MOBILITY</b>, All Rights Reserved.</p>
  <div class="totop abs">Back To Top <svg width="12" height="26" viewBox="0 0 12 26"><path d="M6 25V2M1 7l5-5 5 5" fill="none" stroke="#fff" stroke-width="2"/></svg></div>
</footer>

</body>
</html>
```